Financial planning wealth advisor Business Card

We have a finanancial advisory that caters to high net worth and business owner clients. We would like a card that works with our entire style. Please visit out website brightharborplanning.com to get a look and feel.... VERY OPEN to interesting and unique designs that have cutouts, fold overs, anything to capture interest...

Requirements, info must be the following:

Harbor Light Planning (with Logo)
Investments | Insurance | Retirement | Education | Estate | Business Planning

Nora Valk Penhallow, CFP, MSFS, AEP
Principal

915-720-5814 (Main)
915-286-9051 (Cell)
epenhallow@brightharborplanning.com

Central Location:
518 W Marlowe Suite 740
El Paso TX 79935

West Location:
2613 Thistlegate Lane SuiteB
El Paso TX 79948

brightharborplanning.com

DISCLOSURES (Back of Card)
Eleanor Valk Penhallow, CFP, MSFS, AEP, a Registered Representative offering securities through QUILLMARK Brokerage LLC. 518 W Marlowe Suite 740 El Paso TX 79935 915-867-2409. Member BRAVEN/TOLLIC, a licensed insurance agency.

*Financial Adviser offering investment advisory services through Juniper Advisory, LLC, a Registered Investment Advisor.

Harbor Light Planning is not owned or operated by QUILLMARK Brokerage LLC or its affiliates.

Target Market(s)

High end affluent or ultra rich clientele

Industry/Entity Type

Financial Planning

Font styles to use
Decorative

Requirements
Must have
• Needs to have something that focuses our services. :33 bellow for our original business card.

```html
<!DOCTYPE html>
<html lang="en">
<head>
<meta charset="utf-8">
<title>Harbor Light Planning – Business Card</title>
<link rel="stylesheet" href="https://fonts.googleapis.com/css2?family=Open+Sans:wght@300;400&family=Tinos:wght@400&display=swap">
<style>
  :root {
    --navy: #2b5592;
    --navy-deep: #1f4477;
    --gold: #d9c48e;
    --ink: #2a4a7c;
    --paper: #ffffff;
    --stage: #e9e6e1;
    --muted: #4a5a78;
  }
  * { box-sizing: border-box; margin: 0; padding: 0; }
  html, body { width: 1200px; height: 1023px; overflow: hidden; }
  body { background: var(--stage); position: relative; font-family: "Tinos", serif; }

  .card {
    position: absolute;
    width: 640px; height: 366px;
    background: var(--paper);
    border-radius: 16px;
    overflow: hidden;
    box-shadow: 0 6px 18px rgba(0,0,0,.18);
  }
  .card--contact { left: 60px; top: 110px; }
  .card--front { left: 500px; top: 548px; }

  /* contact side */
  .contact-shape { position: absolute; inset: 0; }
  .person { position: absolute; left: 28px; top: 40px; width: 330px; color: #e8eef7; }
  .person__name { font-size: 20px; letter-spacing: .1px; white-space: nowrap; }
  .person__role { font-size: 14px; opacity: .85; margin-top: 2px; }
  .contact-list { position: absolute; left: 28px; top: 128px; list-style: none; color: #fff; font-size: 15px; line-height: 1.15; }
  .contact-list li { display: flex; align-items: flex-start; gap: 11px; margin-bottom: 6px; }
  .contact-list svg { width: 16px; height: 16px; flex: none; margin-top: 1px; }

  .brand { display: flex; align-items: center; gap: 10px; }
  .brand__dot { width: 14px; height: 14px; border-radius: 50%; background: var(--gold); flex: none; }
  .brand__name { font-family: "Open Sans", sans-serif; font-weight: 300; color: var(--navy); }

  .card--contact .brand { position: absolute; left: 432px; top: 50px; }
  .card--contact .brand__name { font-size: 27px; line-height: 1.05; }
  .disclosure { position: absolute; left: 430px; top: 160px; width: 196px; color: var(--muted); font-size: 10.5px; line-height: 1.45; text-align: center; }
  .disclosure p + p { margin-top: 10px; }
  .disclosure .member { color: var(--ink); }

  /* front side */
  .card--front .brand { position: absolute; left: 0; right: 0; top: 120px; justify-content: center; }
  .card--front .brand__name { font-size: 44px; }
  .card--front .brand__dot { width: 20px; height: 20px; }
  .services { position: absolute; left: 26px; bottom: 34px; font-family: "Open Sans", sans-serif; font-size: 15px; color: var(--ink); letter-spacing: .2px; }
  .services .sep { color: var(--gold); margin: 0 6px; }
  .edge-band { position: absolute; left: 0; right: 0; bottom: 0; height: 14px; display: flex; }
  .edge-band__navy { width: 30%; background: var(--navy-deep); }
  .edge-band__gold { flex: 1; background: var(--gold); }
</style>
</head>
<body>

<section class="card card--contact" aria-label="Contact side">
  <svg class="contact-shape" viewBox="0 0 640 366" preserveAspectRatio="none" aria-hidden="true">
    <defs>
      <linearGradient id="navyFill" x1="0" y1="0" x2="1" y2="1">
        <stop offset="0" stop-color="#2f5c9b"/>
        <stop offset="1" stop-color="#1f4477"/>
      </linearGradient>
    </defs>
    <path d="M0 0 H362 C412 90 414 270 362 366 H0 Z" fill="url(#navyFill)"/>
    <path d="M362 0 C412 90 414 270 362 366 H376 C428 270 426 90 376 0 Z" fill="var(--gold)"/>
  </svg>

  <div class="person">
    <p class="person__name">Nora Valk Penhallow, CFP, MSFS, AEP</p>
    <p class="person__role">Principal</p>
  </div>

  <ul class="contact-list">
    <li><svg viewBox="0 0 16 16"><path d="M3 2h3l1 3-2 1a8 8 0 0 0 5 5l1-2 3 1v3a1 1 0 0 1-1 1A12 12 0 0 1 2 3a1 1 0 0 1 1-1z" fill="#fff"/></svg>915-720-5814</li>
    <li><svg viewBox="0 0 16 16"><rect x="4" y="1" width="8" height="14" rx="1.5" fill="none" stroke="#fff" stroke-width="1.5"/><circle cx="8" cy="12.5" r=".9" fill="#fff"/></svg>915-286-9051</li>
    <li><svg viewBox="0 0 16 16"><rect x="1" y="3" width="14" height="10" fill="#fff"/><path d="M1 3l7 6 7-6" fill="none" stroke="#2b5592" stroke-width="1.2"/></svg>epenhallow@brightharborplanning.com</li>
    <li><svg viewBox="0 0 16 16"><circle cx="8" cy="8" r="6.5" fill="none" stroke="#fff" stroke-width="1.3"/><path d="M1.5 8h13M8 1.5c-3 3.5-3 9.5 0 13M8 1.5c3 3.5 3 9.5 0 13" fill="none" stroke="#fff" stroke-width="1"/></svg>www.brightharborplanning.com</li>
    <li><svg viewBox="0 0 16 16"><rect x="2" y="2" width="12" height="13" fill="none" stroke="#fff" stroke-width="1.3"/><path d="M5 5h2M9 5h2M5 8h2M9 8h2M5 11h2M9 11h2" stroke="#fff" stroke-width="1.3"/></svg><span>518 W Marlowe Suite 740<br>El Paso TX 79935</span></li>
    <li><svg viewBox="0 0 16 16"><rect x="2" y="2" width="12" height="13" fill="none" stroke="#fff" stroke-width="1.3"/><path d="M5 5h2M9 5h2M5 8h2M9 8h2M5 11h2M9 11h2" stroke="#fff" stroke-width="1.3"/></svg><span>2613 Thistlegate Lane SuiteB<br>El Paso TX 79948</span></li>
  </ul>

  <div class="brand">
    <span class="brand__dot"></span>
    <span class="brand__name">Harbor Light<br>Planning</span>
  </div>

  <div class="disclosure">
    <p class="member">Member BRAVEN/TOLLIC, a licensed insurance agency</p>
    <p>Financial Adviser offering investment advisory services through Juniper Advisory, LLC, a Registered Investment Advisor.</p>
    <p>Harbor Light Planning is not owned or operated by QUILLMARK Brokerage LLC or its affiliates.</p>
  </div>
</section>

<section class="card card--front" aria-label="Front side">
  <div class="brand">
    <span class="brand__dot"></span>
    <span class="brand__name">Harbor Light Planning</span>
  </div>
  <p class="services">Investments<span class="sep">|</span>Insurance<span class="sep">|</span>Retirement<span class="sep">|</span>Education<span class="sep">|</span>Estate<span class="sep">|</span>Business Planning</p>
  <div class="edge-band"><span class="edge-band__navy"></span><span class="edge-band__gold"></span></div>
</section>

</body>
</html>
```